Cedar Hollow Drift Tours

We offer guided cross country ( Nordic ) skiing tours in the National Forest bordering Yellowstone National Park. I need a website that attracts individuals by using photos ( provided by me ) , brief descriptions of what to expect, a place with phone numbers to call for a tour, and I would like the website to feature the same color scheme as the logo, which I will upload.

```html
<!DOCTYPE html>
<html lang="en">
<head>
<meta charset="utf-8">
<title>Cedar Hollow Drift Tours</title>
<link href="https://fonts.googleapis.com/css2?family=Montserrat:wght@300;400;500;600;700;800&family=Nunito+Sans:ital,wght@0,400;0,600;0,700;1,400&display=swap" rel="stylesheet">
<style>
:root{
  --purple:#7a85c6;
  --purple-dark:#6570b5;
  --purple-soft:#c8cdec;
  --ink:#222;
  --muted:#555;
  --night:#1d1d1e;
  --white:#fff;
  --snow:#eef0f5;
}
*{box-sizing:border-box;margin:0;padding:0}
html,body{width:1200px;height:3512px;overflow:hidden}
body{position:relative;background:var(--white);font-family:"Nunito Sans",sans-serif;color:var(--ink)}
.abs{position:absolute}
a{color:inherit;text-decoration:none}

/* header */
.site-header{position:absolute;left:0;top:0;width:1200px;height:128px}
.brand{position:absolute;left:106px;top:2px;width:118px;height:118px;border-radius:50%;background:var(--white);box-shadow:0 2px 6px rgba(0,0,0,.2);display:flex;align-items:center;justify-content:center;text-align:center;z-index:3}
.brand-name{font-family:"Montserrat",sans-serif;font-weight:700;font-size:12px;line-height:1.25;color:var(--ink);letter-spacing:.5px;width:88px}
.top-links{position:absolute;right:110px;top:10px;display:flex;gap:34px;font-size:12.5px;color:#333}
.top-links .active{color:var(--purple)}
.toll{position:absolute;right:110px;top:38px;font-family:"Montserrat",sans-serif;font-weight:700;font-size:18px}
.toll span{color:var(--purple)}
.intl{position:absolute;right:112px;top:64px;font-size:11.5px;letter-spacing:.3px;color:#333}
.main-nav{position:absolute;left:0;top:90px;width:1200px;height:38px;background:#000;display:flex;padding-left:230px;font-family:"Montserrat",sans-serif;font-weight:600;font-size:11.5px;color:var(--white)}
.main-nav a{display:flex;align-items:center;padding:0 28px;position:relative}
.main-nav a+a::before{content:"";position:absolute;left:-1px;top:2px;width:1px;height:34px;background:#666;transform:skewX(-25deg)}
.main-nav .hot{background:var(--purple-soft);color:var(--ink);transform:skewX(-20deg)}
.main-nav .hot span{transform:skewX(20deg)}

/* hero */
.hero{position:absolute;left:0;top:128px;width:1200px;height:514px;background:linear-gradient(180deg,#4f7cc4 0%,#8aa9d8 25%,#dfe6f0 45%,#b9c2cc 65%,#5b6570 100%)}
.hero h1{position:absolute;left:0;width:1200px;top:125px;text-align:center;font-family:"Montserrat",sans-serif;font-weight:800;font-size:41px;letter-spacing:5px;color:var(--white)}
.search{position:absolute;left:237px;top:204px;width:665px;height:53px;border-radius:27px;border:4px solid #555;background:var(--white);display:flex;overflow:hidden;font-size:13px;color:#555}
.search .field{display:flex;align-items:center;gap:10px;padding:0 18px;border-right:1px solid #ddd}
.search .dest{width:197px;justify-content:space-between}
.search .date{width:178px}
.search button{flex:1;border:0;background:var(--purple);color:var(--white);font-family:"Montserrat",sans-serif;font-weight:700;font-size:14px;letter-spacing:1.5px}

/* shared heading */
.sec-title{position:absolute;font-family:"Montserrat",sans-serif;font-weight:400;font-size:37px;letter-spacing:6px;padding-left:32px}
.sec-title::before{content:"";position:absolute;left:0;top:-8px;width:58px;height:58px;border:2px solid var(--purple-dark);border-right-color:transparent;border-top-color:var(--purple-dark);border-radius:50%;transform:rotate(-20deg)}
.btn{position:absolute;display:flex;align-items:center;justify-content:center;background:var(--purple);color:var(--white);font-family:"Montserrat",sans-serif;font-weight:700;font-size:13.5px;letter-spacing:1px;border-radius:6px}

/* about */
.about{position:absolute;left:0;top:642px;width:1200px;height:652px;background:linear-gradient(180deg,#fff 0%,#fff 55%,#e7e9ee 80%,#c9ced6 100%)}
.photo{position:absolute;border:none}
.about p{position:absolute;left:628px;top:200px;width:450px;font-size:14.5px;line-height:24px;color:#444}

/* expect */
.expect{position:absolute;left:0;top:1294px;width:1200px;height:637px;background:var(--night);color:var(--white)}
.expect .lead{position:absolute;left:130px;top:150px;width:440px;font-weight:700;font-size:16px;line-height:24px}
.expect p{position:absolute;left:130px;top:215px;width:440px;font-weight:600;font-size:14.5px;line-height:24px}

/* testimonials */
.testimonials{position:absolute;left:0;top:1931px;width:1200px;height:550px}
.card{position:absolute;top:167px;width:478px;height:252px;background:var(--purple-soft);border-radius:4px}
.avatar{position:absolute;left:34px;top:22px;width:118px;height:118px;border-radius:50%;border:4px solid var(--purple-dark);background:linear-gradient(180deg,#aeb5d9,#8791c5)}
.who{position:absolute;left:0;width:188px;top:155px;text-align:center}
.who b{display:block;font-family:"Montserrat",sans-serif;font-weight:600;font-size:15px}
.who small{display:block;font-size:13px;color:#444;margin-top:5px}
.stars{display:flex;justify-content:center;gap:3px;margin-top:6px}
.card q{position:absolute;left:193px;top:42px;width:270px;font-style:italic;font-size:14px;line-height:21.5px;color:#555;quotes:none}
.dots{position:absolute;top:449px;left:546px;display:flex;gap:5px}
.dots i{width:13px;height:13px;border-radius:50%;border:1.5px solid var(--purple-dark)}
.dots i:first-child{background:var(--purple-dark)}

/* contact */
.contact{position:absolute;left:0;top:2481px;width:1200px;height:572px;background:linear-gradient(180deg,#7580c3 0%,#7985c8 50%,#6c77ba 100%)}
.contact .sec-title{color:var(--white)}
.contact .sec-title::before{border-color:var(--white);border-right-color:transparent}
.input{position:absolute;background:var(--white);border-radius:2px;display:flex;align-items:center;gap:12px;padding-left:10px;font-size:11.5px;color:#555}
.input svg{flex:none}
.submit{position:absolute;left:527px;top:443px;width:146px;height:42px;background:var(--white);color:var(--purple);border-radius:4px;display:flex;align-items:center;justify-content:center;font-family:"Montserrat",sans-serif;font-weight:700;font-size:13.5px;letter-spacing:1px}

/* footer */
.site-footer{position:absolute;left:0;top:3053px;width:1200px;height:459px}
.foot-brand{position:absolute;left:118px;top:100px;width:165px;height:165px;border-radius:50%;border:2px solid var(--ink);display:flex;align-items:center;justify-content:center;text-align:center}
.foot-brand span{font-family:"Montserrat",sans-serif;font-weight:700;font-size:16px;line-height:1.3;width:120px}
.foot-title{position:absolute;font-family:"Montserrat",sans-serif;font-size:18px;letter-spacing:3px;padding-left:16px}
.foot-title::before{content:"";position:absolute;left:0;top:-7px;width:34px;height:34px;border:1.5px solid var(--purple-dark);border-right-color:transparent;border-radius:50%;transform:rotate(-20deg)}
.foot-text{position:absolute;left:350px;top:143px;width:300px;font-size:12.5px;line-height:20px;color:#555}
.mail{position:absolute;left:350px;top:212px;width:314px;height:45px;border:1px solid #ccc;font-size:11px;color:#777;display:flex;align-items:center;padding-left:16px}
.foot-list{position:absolute;list-style:none;font-size:11.5px;line-height:24px;color:#555}
.to-top{position:absolute;left:1116px;top:330px;width:40px;height:40px;border-radius:50%;background:var(--purple);display:flex;align-items:center;justify-content:center}
.rule{position:absolute;left:112px;top:350px;width:976px;height:1px;background:#ddd}
.social{position:absolute;left:478px;top:380px;display:flex;gap:32px}
.social i{width:18px;height:18px;border-radius:50%;background:#888}
.copy{position:absolute;left:0;width:1200px;top:417px;text-align:center;font-size:12px;color:#888}
</style>
</head>
<body>

<header class="site-header">
  <div class="brand"><span class="brand-name">CEDAR HOLLOW DRIFT TOURS</span></div>
  <nav class="top-links">
    <a class="active" href="#">Home</a><a href="#">About Us</a><a href="#">Online Check In</a><a href="#">Club</a><a href="#">Blog</a><a href="#">Contact Us</a>
  </nav>
  <div class="toll">TOLL FREE: <span>1-555-014-2290</span></div>
  <div class="intl">INTERNATIONAL DIRECT: 1 (555) 014-3381</div>
  <nav class="main-nav">
    <a href="#">HOME</a><a href="#">BOOK A ROOM</a><a href="#">OUR LOCATIONS</a><a href="#">TRIP PLANNING</a><a class="hot" href="#"><span>HOT DEALS!</span></a><a href="#">SEAVICE &amp; STORAGE</a><a href="#">FAQ</a>
  </nav>
</header>

<section class="hero" role="img" aria-label="Snow-covered mountain range under a blue sky">
  <h1>CEDAR HOLLOW DRIFT TOURS</h1>
  <div class="search">
    <div class="field dest">Destination <svg width="12" height="8"><path d="M0 0h12L6 8z" fill="#222"/></svg></div>
    <div class="field date"><svg width="14" height="14"><rect x="1" y="2" width="12" height="11" fill="none" stroke="#777"/><path d="M1 5h12" stroke="#777"/></svg>Arrival Date</div>
    <div class="field date"><svg width="14" height="14"><rect x="1" y="2" width="12" height="11" fill="none" stroke="#777"/><path d="M1 5h12" stroke="#777"/></svg>Departure Date</div>
    <button>SEARCH</button>
  </div>
</section>

<section class="about">
  <div class="photo abs" style="left:133px;top:83px;width:439px;height:481px;background:linear-gradient(180deg,#c9d0d8,#6f7a72 40%,#dfe3e8 75%,#f4f5f7);box-shadow:0 6px 20px rgba(0,0,0,.35)" role="img" aria-label="Skier on a trail through snow-laden forest"></div>
  <h2 class="sec-title" style="left:620px;top:126px">ABOUT US</h2>
  <p>Perspiciatis unde omnis istenatus errorsit voluptatem accusantium doloremque laudantium, totamrem aperiam eaque ipsa quae ab illo inventore veritatis etquasi archi tecto beatae vitae dicta sunt explicabo. Nemo enim ipsam voluptatem quia voluptas sitaspernatur autodit autfugit sed quia consequuntur magni dolores eos qui ratione volup tatem sequi nesciuntue porro quisquam estquido lorem ipsum quia dolor sit amet, consectetur, adipiscivelit sedquiaafe nonnum quam eius modi tempora incidunt ut labore et dolore magnam aliquam quaerat voluptatem.</p>
  <a class="btn" href="#" style="left:628px;top:473px;width:150px;height:44px">LEARN MORE</a>
</section>

<section class="expect">
  <h2 class="sec-title" style="left:130px;top:79px;color:#fff">WHAT TO EXPECT</h2>
  <div class="lead">Perspiciatis unde omnis istenatus errorsit voluptatem accusantium doloremque laudantium</div>
  <p>Daisnunde omnis istenatus errorsit voluptatem accusantium doloremque laudantium, totamrem aperiam eaque ipsa quae abillo inventore veritatis etquasi archi tecto beatae vitae dicta sunt explicabo. Nemo enim ipsam voluptatem quia voluptasdit autfugit sed quia consequuntur magni dolores eos quiratione volup tatem sequi nesciuntue porro quisquam estquido lorem ipsum quiadolor sitamet consectetur adipiscivelit sedquiaafe nonnum quam eiusmodi tempora incidunt utlaboreet dolore magnam aliquam quaerat voluptatem.</p>
  <a class="btn" href="#" style="left:130px;top:489px;width:173px;height:42px">CALL FOR A TOUR</a>
  <div class="abs" style="left:680px;top:119px;width:365px;height:432px;background:#2e2f31"></div>
  <div class="photo abs" style="left:608px;top:61px;width:367px;height:432px;background:linear-gradient(180deg,#a9b6cc,#c7cfdb 30%,#4d5650 55%,#e7eaee 85%,#f4f5f7);border-radius:3px" role="img" aria-label="Snowy forest clearing with evergreen trees"></div>
</section>

<section class="testimonials">
  <h2 class="sec-title" style="left:434px;top:79px">TESTIMONIALS</h2>
  <div class="card" style="left:112px">
    <div class="avatar" role="img" aria-label="Customer portrait"></div>
    <div class="who"><b>ANNA R HOLT</b><small>May 05, 2021</small>
      <div class="stars"><svg width="84" height="14"><g fill="#111"><path id="s" d="M7 0l2 5h5l-4 3 2 5-5-3-5 3 2-5-4-3h5z"/><use href="#s" x="17"/><use href="#s" x="34"/><use href="#s" x="51"/><use href="#s" x="68"/></g></svg></div></div>
    <q>Perspiciatis unde omnis istenatus errorsit voluptatem accusantium doloremque laudantium, totamrem aperiam eaque ipsa quae ab illo inventore veritatis etquasi archi tecto beatae vitae dicta sunt explicabo. Nemo enim ipsam voluptatem quia voluptas sitaspernatur autodit autfugit.</q>
  </div>
  <div class="card" style="left:610px">
    <div class="avatar" role="img" aria-label="Customer portrait"></div>
    <div class="who"><b>DANIEL K MOSS</b><small>May 05, 2021</small>
      <div class="stars"><svg width="84" height="14"><g fill="#111"><use href="#s"/><use href="#s" x="17"/><use href="#s" x="34"/><use href="#s" x="51"/><use href="#s" x="68"/></g></svg></div></div>
    <q>Perspiciatis unde omnis istenatus errorsit voluptatem accusantium doloremque laudantium, totamrem aperiam eaque ipsa quae ab illo inventore veritatis etquasi archi tecto beatae vitae dicta sunt explicabo. Nemo enim ipsam voluptatem quia voluptas sitaspernatur autodit autfugit.</q>
  </div>
  <div class="dots"><i></i><i></i><i></i><i></i><i></i><i></i></div>
</section>

<section class="contact" role="group" aria-label="Contact form over a tinted winter forest backdrop">
  <h2 class="sec-title" style="left:450px;top:82px">CONTACT US</h2>
  <div class="input" style="left:275px;top:172px;width:311px;height:43px"><svg width="14" height="14"><circle cx="7" cy="4" r="3.5" fill="var(--purple)"/><path d="M1 14c0-5 12-5 12 0z" fill="var(--purple)"/></svg>FIRST NAME</div>
  <div class="input" style="left:612px;top:172px;width:312px;height:43px"><svg width="14" height="14"><circle cx="7" cy="4" r="3.5" fill="var(--purple)"/><path d="M1 14c0-5 12-5 12 0z" fill="var(--purple)"/></svg>LAST NAME</div>
  <div class="input" style="left:275px;top:234px;width:311px;height:43px"><svg width="16" height="12"><rect width="16" height="12" fill="var(--purple)"/><path d="M0 0l8 7 8-7" stroke="#fff" fill="none"/></svg>EMAIL</div>
  <div class="input" style="left:612px;top:234px;width:312px;height:43px"><svg width="14" height="14"><path d="M2 1l3 0 1 3-2 1c1 2 3 4 5 5l1-2 3 1v3c-7 0-11-5-11-11z" fill="var(--purple)"/></svg>PHONE</div>
  <div class="input" style="left:275px;top:296px;width:649px;height:129px;align-items:flex-start;padding-top:12px"><svg width="14" height="14"><path d="M2 2l10 10" stroke="var(--purple)" stroke-width="2"/></svg>WRITE YOUR MESSAGE HERE....</div>
  <a class="submit" href="#">SUBMIT</a>
</section>

<footer class="site-footer">
  <div class="foot-brand"><span>CEDAR HOLLOW DRIFT TOURS</span></div>
  <h3 class="foot-title" style="left:333px;top:120px">NEWSLETTER</h3>
  <p class="foot-text">Perspiciatis undeistenatus errorsit voluptatem accusantium doloremque aperiam eaque.</p>
  <div class="mail">Enter Your Mail</div>
  <a class="btn" href="#" style="left:350px;top:256px;width:150px;height:44px">SUBMIT</a>
  <h3 class="foot-title" style="left:715px;top:120px">QUICK LINKS</h3>
  <ul class="foot-list" style="left:715px;top:150px"><li>Home</li><li>About Us</li><li>Online Check In</li><li>Club</li><li>Blog</li><li>Contact Us</li></ul>
  <h3 class="foot-title" style="left:923px;top:120px">LINKS</h3>
  <ul class="foot-list" style="left:923px;top:150px"><li>FAQ'S</li><li>Terms &amp; Conditions</li><li>Privacy Policy</li><li>Site Map</li><li>Cookies Policy</li></ul>
  <div class="rule"></div>
  <a class="to-top" href="#"><svg width="14" height="10"><path d="M1 9l6-7 6 7" stroke="#fff" stroke-width="2.5" fill="none"/></svg></a>
  <div class="social"><i></i><i></i><i></i><i></i><i></i></div>
  <p class="copy">©2021.ALL RIGHTS RESERVED.</p>
</footer>

</body>
</html>
```